Simple elegant business card

General card for a fin and television director.
Just want name, email, phone and address.

Target Market(s)

Prospective employers

Industry/Entity Type

Business

Requirements
Must have
• As above
Nice to have
• Logo but not necessary.
Should not have
• Not too colourful or funky.
• Simplicity and elegance the way to go.

```html
<!DOCTYPE html>
<html lang="en">
<head>
<meta charset="utf-8">
<title>Lena Marsh – Business Card</title>
<link rel="stylesheet" href="https://fonts.googleapis.com/css2?family=Nothing+You+Could+Do&family=Open+Sans:wght@400&display=swap">
<style>
  :root {
    --page-bg: #e9e7e3;
    --card-front: #f7f7f7;
    --card-back: #1d1d1d;
    --card-back-edge: #141414;
    --ink: #1a1a1a;
    --ink-soft: #2b2b2b;
    --accent: #d42a20;
    --back-script: #3b3b3b;
  }
  * { margin: 0; padding: 0; box-sizing: border-box; }
  html, body {
    width: 1200px;
    height: 676px;
    overflow: hidden;
    background: var(--page-bg);
  }
  .sheet {
    position: relative;
    width: 1200px;
    height: 676px;
    display: flex;
    align-items: center;
    justify-content: center;
    gap: 60px;
  }
  .card {
    position: relative;
    width: 520px;
    height: 297px;
    border-radius: 3px;
    box-shadow: 0 10px 28px rgba(0,0,0,0.18), 0 2px 6px rgba(0,0,0,0.12);
    overflow: hidden;
  }
  .card--front {
    background: linear-gradient(160deg, #ffffff 0%, var(--card-front) 55%, #ececec 100%);
  }
  .card--back {
    background: radial-gradient(ellipse at 40% 30%, #262626 0%, var(--card-back) 55%, var(--card-back-edge) 100%);
  }
  .name-script {
    font-family: "Nothing You Could Do", cursive;
    color: var(--ink);
    white-space: nowrap;
    line-height: 1;
  }
  .card--front .name-script {
    position: absolute;
    left: 52px;
    top: 172px;
    font-size: 46px;
  }
  .contact-list {
    position: absolute;
    left: 282px;
    top: 66px;
    list-style: none;
    font-family: "Open Sans", Arial, sans-serif;
    font-size: 13px;
    line-height: 17px;
    color: var(--ink-soft);
  }
  .contact-list li {
    display: flex;
    align-items: center;
  }
  .contact-icon {
    width: 10px;
    height: 10px;
    margin-right: 7px;
    flex: none;
  }
  .contact-list .no-icon { padding-left: 17px; }
  .card--back .name-script {
    position: absolute;
    left: 70px;
    top: 120px;
    font-size: 112px;
    color: var(--back-script);
    transform: rotate(-4deg);
  }
</style>
</head>
<body>
  <main class="sheet">
    <section class="card card--front" aria-label="Business card front">
      <h1 class="name-script">Lena Marsh</h1>
      <ul class="contact-list">
        <li>
          <svg class="contact-icon" viewBox="0 0 10 10" aria-hidden="true">
            <rect x="0.5" y="2" width="9" height="6.5" rx="0.8" fill="var(--accent)"/>
            <path d="M1 2.6 L5 5.6 L9 2.6" fill="none" stroke="#ffffff" stroke-width="0.9"/>
          </svg>
          lenamarsh@mail.com
        </li>
        <li>
          <svg class="contact-icon" viewBox="0 0 10 10" aria-hidden="true">
            <path d="M2.2 0.8 L3.8 2.8 L2.9 3.9 C3.5 5.3 4.6 6.4 6 7 L7.1 6.1 L9.1 7.7 L8 9.2 C4.5 8.8 1.1 5.4 0.7 1.9 Z" fill="var(--accent)"/>
          </svg>
          +1 310 555 0142
        </li>
        <li class="no-icon">218 Harbor st</li>
        <li class="no-icon">Seaview CA USA</li>
      </ul>
    </section>

    <section class="card card--back" aria-label="Business card back">
      <p class="name-script">Lena Marsh</p>
    </section>
  </main>
</body>
</html>
```